Упаковка для Bright Vega
Задание на дизайн
Приоритеты объектов в упаковке
Зонтичная марка, Знак производителя, Марка продукта, Вид продукта, Название продукта, Иллюстрация
Размеры
Опишите свою организацию или продукт и целевую аудиторию
Производство и продажа электро-, бензо-, аккумуляторного инструмента для строительства и ремонта.
Существующая упаковка .То, что хочется обновить.
Образец существующей упаковки.
Комментарии и пожелания для дизайнеров
Необходимо полностью обновить устаревший дизайн упаковки для инструмента, на примере шуруповерта. Фирменный красный цвет, а также сам логотип и сочетания цветов внутри него менять нельзя. Логотип обязательно должен присутствовать на упаковке. Название серии Zet power line должно остаться, но в любом другом виде и написании. Остальное можно менять до неузнаваемости. Фото инструмента должно быть помещено на упаковку целиком. Упаковка должна быть современной, сочной, красочной, информативной и обязательно несложно адаптивной под другие виды инструмента и форматы коробок (ушм, перфораторы, лобзики и пр.). Другие образцы наших упаковок можно легко найти в сети.

```html
<!DOCTYPE html>
<html lang="ru">
<head>
<meta charset="utf-8">
<title>Bright Vega — дрель бесщеточная аккумуляторная</title>
<link rel="stylesheet" href="https://fonts.googleapis.com/css2?family=Oswald:wght@400;500;600&family=Roboto:wght@700&display=swap">
<style>
  :root {
    --bg: #ffffff;
    --panel-dark: #1c1c1c;
    --panel-mid: #3a3a3a;
    --handle: #151515;
    --brand-red: #b3191c;
    --text-white: #ffffff;
    --text-grey: #d4d4d4;
    --text-muted: #c9c9c9;
  }
  html, body {
    margin: 0;
    width: 1200px;
    height: 958px;
    overflow: hidden;
    background: var(--bg);
  }
  .package-front {
    position: absolute;
    left: 141px;
    top: 107px;
    width: 906px;
    height: 739px;
    background: radial-gradient(ellipse at 40% 45%, var(--panel-mid) 0%, var(--panel-dark) 75%);
    overflow: hidden;
    font-family: "Oswald", "Arial Narrow", sans-serif;
    color: var(--text-white);
  }
  .red-field {
    position: absolute;
    left: 0;
    top: 0;
    width: 906px;
    height: 739px;
  }
  .series-mark {
    position: absolute;
    left: 62px;
    top: 32px;
    display: flex;
    align-items: center;
    gap: 10px;
    white-space: nowrap;
  }
  .series-mark .square {
    width: 22px;
    height: 22px;
    background: var(--brand-red);
  }
  .series-mark .name {
    font-weight: 600;
    font-size: 30px;
    letter-spacing: 0.5px;
    text-transform: uppercase;
    line-height: 1;
  }
  .model-code {
    position: absolute;
    left: 62px;
    top: 150px;
    font-size: 21px;
    line-height: 1;
    color: var(--text-grey);
    letter-spacing: 0.3px;
    white-space: nowrap;
  }
  .product-type {
    position: absolute;
    left: 60px;
    top: 192px;
    margin: 0;
    font-weight: 500;
    line-height: 1;
    text-transform: uppercase;
    white-space: nowrap;
  }
  .product-type .main { display: block; font-size: 76px; }
  .product-type .sub { display: block; font-size: 47px; margin-top: 14px; }
  .divider {
    position: absolute;
    left: 62px;
    top: 407px;
    width: 345px;
    height: 3px;
    background: var(--text-white);
  }
  .power-spec {
    position: absolute;
    left: 61px;
    top: 418px;
    font-size: 50px;
    font-weight: 500;
    color: var(--text-grey);
    line-height: 1.1;
  }
  .spec {
    position: absolute;
    color: var(--text-muted);
    text-transform: uppercase;
    white-space: nowrap;
  }
  .spec .value {
    display: block;
    font-family: "Roboto", Arial, sans-serif;
    font-weight: 700;
    font-size: 21px;
    line-height: 1.1;
    text-transform: none;
  }
  .spec .label {
    display: block;
    font-size: 17px;
    line-height: 26px;
    margin-top: 4px;
  }
  .spec-chuck { left: 62px; top: 493px; }
  .spec-torque { left: 231px; top: 493px; }
  .spec-drill { left: 62px; top: 559px; }
  .spec-steps { left: 231px; top: 559px; }
  .spec-speed { left: 62px; top: 651px; }
  .brand-name {
    position: absolute;
    left: 630px;
    top: 52px;
    display: flex;
    align-items: center;
    gap: 10px;
    white-space: nowrap;
  }
  .brand-name .square {
    width: 22px;
    height: 22px;
    background: var(--text-white);
  }
  .brand-name .name {
    font-weight: 600;
    font-size: 40px;
    line-height: 1;
    text-transform: uppercase;
  }
  .tool-photo {
    position: absolute;
    left: 500px;
    top: 168px;
    width: 350px;
    height: 550px;
    border-radius: 40px 40px 24px 24px;
    background: radial-gradient(ellipse at 55% 50%, #d8393b 0%, #8e1a1c 45%, #2a1a1a 80%, rgba(42,26,26,0.35) 100%);
  }
</style>
</head>
<body>
  <main class="package-front">
    <svg class="red-field" viewBox="0 0 906 739" aria-hidden="true">
      <polygon points="606,0 906,0 906,739 381,739 453,130 606,130" fill="var(--brand-red)"/>
      <rect x="304" y="0" width="302" height="130" fill="var(--handle)"/>
    </svg>

    <div class="series-mark">
      <span class="square"></span>
      <span class="name">Zet power line</span>
    </div>

    <div class="model-code">BV320/2.0-KDX-LN-4A</div>

    <h1 class="product-type">
      <span class="main">Дрель</span>
      <span class="sub">бесщеточная</span>
      <span class="sub">аккумуляторная</span>
    </h1>

    <div class="divider"></div>
    <div class="power-spec">20V/2.0Ah</div>

    <div class="spec spec-chuck"><span class="value">10 мм</span><span class="label">диаметр патрона</span></div>
    <div class="spec spec-torque"><span class="value">40 Нм</span><span class="label">max крутящий момент</span></div>
    <div class="spec spec-drill"><span class="value">10 мм</span><span class="label">max диаметр<br>сверления в стали</span></div>
    <div class="spec spec-steps"><span class="value">23+1</span><span class="label">ступени крутящего<br>момента</span></div>
    <div class="spec spec-speed"><span class="value">0-500 об/мин / 0-1650 об/мин</span><span class="label">скорость холостого хода</span></div>

    <div class="brand-name">
      <span class="square"></span>
      <span class="name">Bright Vega</span>
    </div>

    <div class="tool-photo" role="img" aria-label="Фото аккумуляторной бесщеточной дрели с аккумулятором 20V 2.0Ah в красно-черном корпусе"></div>
  </main>
</body>
</html>
```